need web page design for TarnwickHub.com

This site sells information products for international corporate users. It is selling Silent Rivers and Quiet Orchard Lanes, a product on international business tax, and other books. See sample. I will also upload a possible logo. Upload 2 The tag line is Predicting and Solving Business and Law Issues for the Multinational Upload 3 is a sample theme from Shopify, the site I will use. The sample is for ideas only. I am not wedded to it. Upload 4 is Copperfield Monthly Digest Pge

2 page

```html
<!DOCTYPE html>
<html lang="en">
<head>
<meta charset="utf-8">
<title>TarnwickHub.com</title>
<link href="https://fonts.googleapis.com/css2?family=Lato:ital,wght@0,400;0,700;1,400&family=Oswald:wght@400;500&display=swap" rel="stylesheet">
<style>
:root{
  --navy:#0d2a80;
  --navy-dark:#08205c;
  --ink:#333;
  --muted:#555;
  --link:#13318a;
  --panel:#f3f3f3;
  --line:#d6d6d6;
  --white:#fff;
}
*{box-sizing:border-box;margin:0;padding:0}
html,body{width:827px;height:1200px;overflow:hidden;background:var(--white)}
body{position:relative;font-family:'Lato',sans-serif;color:var(--ink)}
.abs{position:absolute}
.heading{font-family:'Oswald',sans-serif;font-weight:500;color:var(--navy)}
.heading .soft{color:var(--muted);font-weight:400}

/* header */
.brand{left:0;width:827px;top:14px;text-align:center}
.brand-mark{width:40px;height:40px;border-radius:50%;background:var(--navy);margin:0 auto 6px}
.brand-name{font-family:'Lato',sans-serif;font-weight:700;font-size:14px;color:var(--navy);line-height:1}
.brand-tag{font-size:5px;color:var(--muted);margin-top:2px}
.rule-top{left:90px;top:92px;width:647px;height:1px;background:#bbb}
.nav{left:90px;top:96px;width:394px;height:26px;background:var(--navy);display:flex;align-items:center}
.nav a{color:var(--white);text-decoration:none;font-size:10.5px;padding:0 15px;height:26px;line-height:26px;border-right:1px solid #2a4698}
.nav a:last-child{border-right:0}
.nav a.active{background:#0a2266;border-bottom:2px solid #8aa0d8;padding:0 19px}
.search{left:491px;top:96px;width:142px;height:26px;background:#8f8f8f;color:#eee;font-size:9.5px;font-style:italic;padding:8px 7px}
.search svg{position:absolute;right:7px;top:7px}
.cart{left:640px;top:96px;width:97px;height:26px;background:var(--navy);color:var(--white);font-size:10px;display:flex;align-items:center;gap:5px;padding-left:7px}
.cart b{font-size:12px;font-weight:400}

/* hero */
.hero{left:0;top:124px;width:827px;height:322px;background:linear-gradient(90deg,#f3d4c8 0%,#e4e4da 35%,#d6e6e3 70%,#cfdedb 100%)}
.hero-photo{left:96px;top:10px;width:256px;height:312px;background:linear-gradient(180deg,#cfb3a3 0%,#2d2d33 45%,#1d1d22 100%);border-radius:120px 120px 0 0}
.hero-dot{left:536px;top:104px;width:36px;height:36px;border-radius:50%;background:var(--navy)}
.hero-title{left:360px;top:156px;width:388px;text-align:center;font-family:'Oswald',sans-serif;font-weight:500;font-size:27px;line-height:34px;color:var(--navy)}

/* products */
.section-title{left:0;width:827px;top:466px;text-align:center;font-size:21px}
.title-rule{left:154px;top:499px;width:518px;height:1px;background:var(--line)}
.title-accent{left:354px;top:498px;width:118px;height:2px;background:var(--navy)}
.card{top:516px;width:148px;height:268px;background:#f1f1f1;border:1px solid #e6e6e6}
.card-inner{position:absolute;left:4px;top:4px;width:138px;height:180px;background:var(--white)}
.cover{position:absolute;left:16px;top:10px;width:106px;height:158px}
.card-name{position:absolute;top:190px;left:0;width:146px;text-align:center;font-size:10.5px;line-height:13.5px;color:var(--ink)}
.price{position:absolute;top:229px;left:40px;width:67px;height:22px;background:var(--navy);color:var(--white);font-weight:700;font-size:11.5px;text-align:center;line-height:22px}

/* info band */
.band{left:0;top:804px;width:827px;height:213px;background:var(--panel)}
.col-title{font-size:18px;top:826px}
.col-rule{top:849px;height:1px;background:var(--line)}
.col-accent{top:848px;height:2px;background:var(--navy)}
.about-text{left:92px;top:861px;width:310px;font-size:8.8px;line-height:14.5px;color:var(--ink)}
.btn{left:92px;top:970px;width:67px;height:22px;background:var(--navy);color:var(--white);font-size:10.5px;text-align:center;line-height:22px}
.arrow-box{top:829px;width:15px;height:15px;border:1px solid #bbb;background:#f8f8f8}
.post-thumb{left:431px;width:61px;height:62px;border:2px solid var(--white)}
.post{left:502px;width:230px;font-size:8.8px;line-height:14.5px}
.post .date{font-style:italic;color:var(--ink)}
.post .title{font-weight:700;color:var(--link)}

/* footer */
.footer{left:0;top:1017px;width:827px;height:150px;background:var(--navy)}
.foot-title{top:1037px;font-family:'Oswald',sans-serif;font-size:14px;color:var(--white)}
.foot-rule{top:1064px;height:1px;background:#2e4fa5}
.foot-links{left:91px;top:1074px;font-size:8.5px;line-height:15.2px;color:var(--white);list-style:none}
.contact-row{left:231px;display:flex;gap:8px;color:var(--white);font-size:8.5px;line-height:12px;align-items:center}
.icon-sq{width:19px;height:19px;background:#08205c;display:flex;align-items:center;justify-content:center;flex:none}
.news-date{left:410px;top:1075px;width:29px;height:37px;background:#08205c;color:var(--white);text-align:center;font-size:10px;line-height:12px;padding-top:6px}
.news-text{left:449px;top:1074px;width:122px;font-size:8.3px;line-height:11.8px;color:var(--white)}
.news-more{left:512px;top:1134px;font-size:8.5px;font-weight:700;color:var(--white)}
.nl-text{left:604px;top:1074px;width:140px;font-size:8.5px;line-height:12px;color:var(--white)}
.nl-input{left:604px;top:1103px;width:133px;height:22px;background:#eee;border:1px solid #ccc;font-size:8px;color:#777;padding:6px 5px}
.nl-btn{left:604px;top:1131px;width:67px;height:21px;background:#08205c;color:var(--white);font-size:10px;text-align:center;line-height:21px}
.bottom{left:0;top:1167px;width:827px;height:33px;background:var(--navy-dark)}
.copy{left:91px;top:1179px;font-size:8.5px;color:var(--white)}
.social{top:1174px;width:18px;height:18px;border-radius:50%;background:#3a4f88}
.pay{top:1176px;width:25px;height:16px;border-radius:2px;background:#d8dde8}
</style>
</head>
<body>

<header>
  <div class="abs brand">
    <div class="brand-mark"></div>
    <div class="brand-name">TarnwickHub.com</div>
    <div class="brand-tag">Business and Law Solutions for Multinational Companies</div>
  </div>
  <div class="abs rule-top"></div>
  <nav class="abs nav">
    <a class="active">Home</a><a>Catalog</a><a>Blog</a><a>About Us</a><a>Doing Business Guides</a>
  </nav>
  <div class="abs search">Search
    <svg width="11" height="11" viewBox="0 0 12 12"><circle cx="5" cy="5" r="3.8" fill="none" stroke="#fff" stroke-width="1.6"/><line x1="7.8" y1="7.8" x2="11" y2="11" stroke="#fff" stroke-width="1.8"/></svg>
  </div>
  <div class="abs cart">
    <svg width="12" height="11" viewBox="0 0 12 11"><path d="M0 1h2l1.6 6h6.4L11.5 2.5H3" fill="none" stroke="#fff" stroke-width="1.4"/><circle cx="4.5" cy="9.5" r="1.1" fill="#fff"/><circle cx="9" cy="9.5" r="1.1" fill="#fff"/></svg>
    <span><b>0</b> Item - $0.00</span>
  </div>
</header>

<section class="abs hero">
  <div class="abs hero-photo" role="img" aria-label="Photo of a smiling businessman in a dark suit with arms crossed"></div>
  <div class="abs hero-dot"></div>
  <h1 class="abs hero-title">Predicting and Solving Business and Law Issues for the Multinational</h1>
</section>

<h2 class="abs heading section-title"><span class="soft">Our</span> Products</h2>
<div class="abs title-rule"></div>
<div class="abs title-accent"></div>

<div class="abs card" style="left:90px">
  <div class="card-inner"><div class="cover" role="img" aria-label="Book cover with a cargo ship on a teal background" style="background:linear-gradient(180deg,#3c6b70 0%,#5d7f88 40%,#364c50 75%,#2e5a5e 100%)"></div></div>
  <div class="card-name">Silent Rivers and Quiet<br>Orchard Lanes</div>
  <div class="price">$195.00</div>
</div>
<div class="abs card" style="left:257px">
  <div class="card-inner"><div class="cover" role="img" aria-label="Dark book cover with a container ship and orange title text" style="background:linear-gradient(180deg,#6b7680 0%,#3b3b3b 40%,#1e1e1e 100%)"></div></div>
  <div class="card-name">Silent Rivers and Quiet<br>Orchard Lanes</div>
  <div class="price">$195.00</div>
</div>
<div class="abs card" style="left:422px">
  <div class="card-inner"><div class="cover" role="img" aria-label="Maroon book cover with a world map and currency image" style="background:linear-gradient(180deg,#7a1e35 0%,#5c2a5a 45%,#8a2a40 100%)"></div></div>
  <div class="card-name">Silent Rivers and Quiet<br>Orchard Lanes</div>
  <div class="price">$195.00</div>
</div>
<div class="abs card" style="left:588px">
  <div class="card-inner"><div class="cover" role="img" aria-label="White and black book cover with a yellow stripe" style="background:linear-gradient(180deg,#f2c13a 0%,#fff 6%,#fff 55%,#111 58%,#111 100%)"></div></div>
  <div class="card-name">Silent Rivers and Quiet<br>Orchard Lanes</div>
  <div class="price">$195.00</div>
</div>

<section>
  <div class="abs band"></div>
  <h2 class="abs heading col-title" style="left:92px"><span class="soft">About</span> Us</h2>
  <div class="abs col-rule" style="left:92px;width:308px"></div>
  <div class="abs col-accent" style="left:92px;width:83px"></div>
  <p class="abs about-text">It is a long established fact that a reader will be distracted by the reada content of a page when looking at its layout. The point of using Lorem Ipsum is that has a more-or-less normal distribution of letters, as opposed to using 'Conte here, content here', making it look like readable English. Many desktop pub packages and web page editors now use Lorem Ipsum as their default model text, search for 'lorem ipsum' will uncover many web sites still in their infancy. Va versions have evolved over the years.</p>
  <div class="abs btn">Read More</div>

  <h2 class="abs heading col-title" style="left:429px"><span class="soft">Latest</span> Post</h2>
  <div class="abs col-rule" style="left:429px;width:308px"></div>
  <div class="abs col-accent" style="left:429px;width:83px"></div>
  <div class="abs arrow-box" style="left:699px"><svg width="13" height="13" viewBox="0 0 13 13"><path d="M8 3L5 6.5L8 10" fill="none" stroke="#777" stroke-width="1"/></svg></div>
  <div class="abs arrow-box" style="left:722px"><svg width="13" height="13" viewBox="0 0 13 13"><path d="M5 3L8 6.5L5 10" fill="none" stroke="#777" stroke-width="1"/></svg></div>

  <div class="abs post-thumb" style="top:862px;background:linear-gradient(180deg,#c9c2b4,#7a5a45)" role="img" aria-label="Portrait of a smiling man"></div>
  <div class="abs post" style="top:864px"><div class="date">01/10/2014</div><div class="title">Lorem Ipsum is simply dummy</div><div>printing and typesetting industry. Lorem Ipsum has been the industry's standard dummy text ever since</div></div>
  <div class="abs post-thumb" style="top:936px;background:linear-gradient(180deg,#e8ddd0,#c9a878)" role="img" aria-label="Portrait of a smiling woman"></div>
  <div class="abs post" style="top:937px"><div class="date">01/10/2014</div><div class="title">Lorem Ipsum is simply dummy</div><div>printing and typesetting industry. Lorem Ipsum has been the industry's standard dummy text ever since</div></div>
</section>

<footer>
  <div class="abs footer"></div>
  <h3 class="abs foot-title" style="left:91px">Quick Links</h3>
  <div class="abs foot-rule" style="left:91px;width:112px"></div>
  <ul class="abs foot-links"><li>› Home</li><li>› Catalog</li><li>› Blog</li><li>› About Us</li><li>› Doing Business Guides</li></ul>

  <h3 class="abs foot-title" style="left:230px">Contact Us</h3>
  <div class="abs foot-rule" style="left:230px;width:142px"></div>
  <div class="abs contact-row" style="top:1072px"><span class="icon-sq"><svg width="8" height="10" viewBox="0 0 8 10"><path d="M4 0a3.5 3.5 0 0 0-3.5 3.5C.5 6 4 10 4 10s3.5-4 3.5-6.5A3.5 3.5 0 0 0 4 0z" fill="#fff"/><circle cx="4" cy="3.5" r="1.2" fill="#08205c"/></svg></span>1234 Lorem, established, USA</div>
  <div class="abs contact-row" style="top:1094px"><span class="icon-sq"><svg width="9" height="9" viewBox="0 0 10 10"><path d="M2 0l2 2.5-1.2 1.3a6 6 0 0 0 3.4 3.4L7.5 6 10 8l-1.5 2C4 10 0 6 0 1.5z" fill="#fff"/></svg></span>(123) 3456 7890<br>(123) 3456 7890</div>
  <div class="abs contact-row" style="top:1123px"><span class="icon-sq"><svg width="9" height="7" viewBox="0 0 9 7"><rect width="9" height="7" fill="#fff"/><path d="M0 0l4.5 4L9 0" fill="none" stroke="#08205c" stroke-width="1"/></svg></span>support@tarnwickhub.com</div>

  <h3 class="abs foot-title" style="left:410px">Latest News</h3>
  <div class="abs foot-rule" style="left:410px;width:161px"></div>
  <div class="abs news-date">18<br>Mar</div>
  <p class="abs news-text">Duis autem vel eum iriure hendrerit in vulputate velit esse m consequat, vel illum dolore eu feugiat n facilisis at vero eros et accumsan.</p>
  <div class="abs news-more">read all news »</div>

  <h3 class="abs foot-title" style="left:604px">NewsLetter Signup</h3>
  <div class="abs foot-rule" style="left:604px;width:133px"></div>
  <p class="abs nl-text">Subscribe to our newsletter to recieve special offers and discount.</p>
  <div class="abs nl-input">Enter your Email Id</div>
  <div class="abs nl-btn">Subscribe</div>

  <div class="abs bottom"></div>
  <div class="abs copy">Copyright © 2014 TarnwickHub.com</div>
  <div class="abs social" style="left:580px"></div>
  <div class="abs social" style="left:602px"></div>
  <div class="abs social" style="left:625px"></div>
  <div class="abs pay" style="left:654px"></div>
  <div class="abs pay" style="left:683px"></div>
  <div class="abs pay" style="left:711px"></div>
</footer>

</body>
</html>
```